Book Cover RE-Design Project (front/back)

I have a book cover designed in the early 90's that is severely outdated and I need a complete redesign of it.

It is for a parenting book called "Raising Roots"

I'm looking for a fresh, new, clean design - not a remake of the old cover. I will attach the old cover simply as a reference for the copy/text that should be included on the front and back.

The book is about parenting for people with kids of all ages. The current design is too "child" oriented (photos and colors) and the feeling is that the book is for only parents with younger children, when in fact the book's principles are universal for young children, teenagers, and even troubled/severely troubled teenagers.

The design should communicate that the book is authoritative, and easy to implement. Authoritative as in a bestselling book/author celebrity author rather than a college professor essay. Easy to implement as in the book give you a specific plan/blueprint rather than just a bunch of psychology ideas.

There should be some kind of "orange" element in the design since it is one of 4 books in a set and the content of the books reference the other books by color (orange, blue, green, red) - but the color does not need to be the entire cover as it is currently. If the 4 books were together you would be able to easily identify which was the blue, orange, green or red book.

The current photos show "happy families" and young children, but like said above the photos of only young children exclude the books effectiveness for older children and teens. The "happy families" photos also seem to convey an "infomercial" feel that I don't like because it feels a little staged/stock and possibly unobtainable. I would like to leave the image of an ideal outcome/family to the imagination of the reader, so photos of people/families are not necessary - but photos are not out of the question.

The logo "theFamily Compass" will be attached to the project files for inclusion.

The logo "Northfield Household Academy" on the current cover will NOT be included on the new cover.
Updates

Reason: This is my first project with Artisfold and I think I should have more time to interact with the designers.

Target Market(s)

Parents 30-50 who are dealing with kids (all ages - especially teens) who are defiant, lazy, and out of control.

Industry/Entity Type

College

Requirements
Must have
• 1. Some kid of "Orange" element identifying the book as the orange book in the set of (orange, red, blue, green) The actual color of the orange element can be left up to the designer.
2. The number 1 - identifying it as #1 in the set.
3. Dr. Walter Pemberly as the author
4. The bullet points on front cover (see original cover attached to project)
5. Text/copy on back cover (see original cover attached to project)

```html
<!DOCTYPE html>
<html lang="en">
<head>
<meta charset="utf-8">
<title>Raising Roots – Cover Layout</title>
<link rel="stylesheet" href="https://fonts.googleapis.com/css2?family=Didact+Gothic&family=Poppins:wght@300;600;700&display=swap">
<style>
  :root {
    --orange: #f7a93b;
    --orange-soft: #fbc879;
    --ink: #1b1b1b;
    --paper: #ffffff;
    --guide: #8a8a8a;
  }
  * { box-sizing: border-box; margin: 0; padding: 0; }
  html, body { width: 1200px; height: 1182px; overflow: hidden; background: var(--paper); }
  body { position: relative; font-family: "Didact Gothic", "Century Gothic", sans-serif; color: var(--ink); }

  .panel { position: absolute; background: var(--paper); }
  .panel--outlined { border: 1px solid #d6d6d6; }

  /* Back cover */
  .back-stripe { position: absolute; background: var(--orange); }
  .back-copy { position: absolute; font-size: var(--fs); line-height: 1.3; }
  .back-copy .series { font-size: calc(var(--fs) * 1.35); margin-bottom: 2px; }
  .back-copy .headline { font-family: "Poppins", sans-serif; font-weight: 700; font-size: calc(var(--fs) * 1.6); margin-bottom: calc(var(--fs) * 1.1); }
  .back-copy p { margin-bottom: calc(var(--fs) * 1.1); }
  .back-copy ul { list-style: none; margin-bottom: calc(var(--fs) * 1.1); }
  .back-copy li { position: relative; padding-left: calc(var(--fs) * 1.4); margin-bottom: calc(var(--fs) * 0.55); }
  .back-copy li::before { content: "★"; position: absolute; left: 0; top: 0; color: var(--orange); }

  /* Spine */
  .spine { position: absolute; background: var(--orange); overflow: hidden; }
  .spine span { position: absolute; writing-mode: vertical-rl; white-space: nowrap; line-height: 1; }
  .spine .series { font-family: "Poppins", sans-serif; font-weight: 300; color: var(--ink); }
  .spine .title { font-family: "Poppins", sans-serif; font-weight: 700; color: var(--ink); }
  .spine .author { font-family: "Poppins", sans-serif; font-weight: 600; color: var(--paper); }

  /* Front cover */
  .front .series { position: absolute; font-family: "Didact Gothic", sans-serif; }
  .front .title { position: absolute; font-family: "Poppins", sans-serif; font-weight: 700; line-height: 1; }
  .front .author { position: absolute; font-family: "Didact Gothic", sans-serif; }
  .front .artwork { position: absolute; background: linear-gradient(180deg, var(--orange-soft), #fde6c2); border-radius: 6px; }
  .front .volume { position: absolute; border: 2px solid var(--orange); border-radius: 50%; color: var(--orange);
    font-family: "Poppins", sans-serif; font-weight: 600; line-height: 1; display: flex; align-items: center; justify-content: center; }
  .front .topics { position: absolute; list-style: none; line-height: 1.4; white-space: nowrap; }
  .front .topics li::before { content: "★ "; color: var(--orange); }

  /* Dimension guides */
  .guides { position: absolute; left: 0; top: 0; }
  .dim-label { position: absolute; font-family: "Poppins", sans-serif; font-weight: 600; font-size: 20px; color: var(--ink);
    background: var(--paper); padding: 0 6px; white-space: nowrap; }
</style>
</head>
<body>

<!-- Row 1: separate panels -->
<section class="panel back" style="left:0; top:0; width:372px; height:467px;">
  <div class="back-stripe" style="left:0; top:0; width:21px; height:467px;"></div>
  <div class="back-copy" style="--fs:8.6px; left:30px; top:40px; width:325px;">
    <div class="series">The Family Compass</div>
    <div class="headline">Raising Roots - Your starting Point</div>
    <p>A key part of your bond with your children rests on their behavior. How well they listen, how they handle their chores and how they follow your house rules shapes how you treat them each day. That is why Raising Roots is a useful and vital part of The Family Compass.</p>
    <p>Kids of every age test limits. When you know what drives their choices, you can respond with calm and a clear plan. That is why Raising Roots sits at the core of The Family Compass.</p>
    <ul>
      <li>The short sessions hold a lifetime of value, and you will find yourself returning to them often. Here are a few tools you will learn and want to review.</li>
      <li>The Pleasure Principle in Chapter 2 is a strong idea that helps you see why kids behave as they do.</li>
      <li>A key to changing behavior is through consequences, an essential part of learning. Use them well (Page 5)</li>
      <li>Should you ever negotiate consequences? See Page 7.</li>
      <li>The 5 steps to pinpointing a problem behavior. It's that simple (Page 13)</li>
      <li>Go to Chapter 7 to find out how we reward good choices.</li>
      <li>Punishment is a hard topic for many parents. On Page 40, you learn the four types and when to use each.</li>
      <li>Time Out may be the most misused tool. You'll learn the right length on Page 42.</li>
      <li>Chapter 11 is all about the Color Code, one of the most useful ideas in The Family Compass.</li>
    </ul>
    <p>Be sure to jot notes in the Notes section at the end of each chapter. It keeps all your key points in one place. The glossary at the back lists over 140 terms for quick reference.</p>
  </div>
</section>

<section class="spine" style="left:540px; top:0; width:110px; height:467px;">
  <span class="title" style="left:20px; top:14px; font-size:36px;">Raising Roots</span>
  <span class="series" style="left:68px; top:16px; font-size:17px;">The Family Compass</span>
  <span class="author" style="left:31px; top:288px; font-size:16px;">Dr. Walter Pemberly</span>
</section>

<section class="panel panel--outlined front" style="left:872px; top:0; width:328px; height:467px;">
  <div class="series" style="left:26px; top:48px; font-size:15px;">The Family Compass</div>
  <div class="title" style="left:26px; top:66px; font-size:30px;">Raising Roots</div>
  <div class="author" style="left:26px; top:104px; font-size:13px;">Dr. Walter Pemberly</div>
  <div class="artwork" role="img" aria-label="Cluster of orange balloons carrying family and household icons" style="left:16px; top:128px; width:290px; height:208px;"></div>
  <div class="volume" style="left:256px; top:342px; width:28px; height:28px; font-size:16px;">1</div>
  <ul class="topics" style="left:172px; top:378px; font-size:11.5px;">
    <li>Behavior Modification</li>
    <li>Consequences</li>
    <li>Punishment</li>
    <li>Personality Codes</li>
  </ul>
</section>

<!-- Row 2: flat spread with dimensions -->
<svg class="guides" width="1200" height="1182" viewBox="0 0 1200 1182" aria-hidden="true">
  <g stroke="var(--guide)" stroke-width="1" fill="none">
    <line x1="222" y1="520" x2="222" y2="1182"/>
    <line x1="540" y1="520" x2="540" y2="1182"/>
    <line x1="650" y1="520" x2="650" y2="1182"/>
    <line x1="980" y1="520" x2="980" y2="1182"/>
    <line x1="180" y1="605" x2="1090" y2="605"/>
    <line x1="180" y1="1097" x2="1090" y2="1097"/>
  </g>
</svg>

<div class="back-stripe" style="left:196px; top:579px; width:49px; height:518px;"></div>

<section class="panel back" style="left:245px; top:605px; width:295px; height:492px; border-top:1px solid #d6d6d6; border-bottom:1px solid #d6d6d6;">
  <div class="back-copy" style="--fs:7.4px; left:27px; top:118px; width:250px;">
    <div class="series">The Family Compass</div>
    <div class="headline">Raising Roots - Your starting Point</div>
    <p>A key part of your bond with your children rests on their behavior. How well they listen, how they handle their chores and how they follow your house rules shapes how you treat them each day. That is why Raising Roots is a useful and vital part of The Family Compass.</p>
    <p>Kids of every age test limits. When you know what drives their choices, you can respond with calm and a clear plan. That is why Raising Roots sits at the core of The Family Compass.</p>
    <ul>
      <li>The short sessions hold a lifetime of value, and you will find yourself returning to them often. Here are a few tools you will learn and want to review.</li>
      <li>The Pleasure Principle in Chapter 2 is a strong idea that helps you see why kids behave as they do.</li>
      <li>A key to changing behavior is through consequences, an essential part of learning. Use them well (Page 5)</li>
      <li>Should you ever negotiate consequences? See Page 7.</li>
      <li>The 5 steps to pinpointing a problem behavior. It's that simple (Page 13)</li>
      <li>Go to Chapter 7 to find out how we reward good choices.</li>
      <li>Punishment is a hard topic for many parents. On Page 40, you learn the four types and when to use each.</li>
      <li>Time Out may be the most misused tool. You'll learn the right length on Page 42.</li>
      <li>Chapter 11 is all about the Color Code, one of the most useful ideas in The Family Compass.</li>
    </ul>
    <p>Be sure to jot notes in the Notes section at the end of each chapter. It keeps all your key points in one place. The glossary at the back lists over 140 terms for quick reference.</p>
  </div>
</section>

<section class="spine" style="left:540px; top:579px; width:110px; height:518px;">
  <span class="title" style="left:19px; top:16px; font-size:38px;">Raising Roots</span>
  <span class="series" style="left:68px; top:18px; font-size:18px;">The Family Compass</span>
  <span class="author" style="left:30px; top:306px; font-size:17px;">Dr. Walter Pemberly</span>
</section>

<section class="panel front" style="left:650px; top:605px; width:330px; height:492px; border-top:1px solid #d6d6d6; border-bottom:1px solid #d6d6d6;">
  <div class="series" style="left:28px; top:40px; font-size:17px;">The Family Compass</div>
  <div class="title" style="left:28px; top:60px; font-size:31px;">Raising Roots</div>
  <div class="author" style="left:28px; top:104px; font-size:14px;">Dr. Walter Pemberly</div>
  <div class="artwork" role="img" aria-label="Cluster of orange balloons carrying family and household icons" style="left:20px; top:130px; width:296px; height:195px;"></div>
  <div class="volume" style="left:264px; top:334px; width:30px; height:30px; font-size:17px;">1</div>
  <ul class="topics" style="left:176px; top:374px; font-size:12.5px;">
    <li>Behavior Modification</li>
    <li>Consequences</li>
    <li>Punishment</li>
    <li>Personality Codes</li>
  </ul>
</section>

<svg class="guides" width="1200" height="1182" viewBox="0 0 1200 1182" aria-hidden="true">
  <g stroke="var(--ink)" stroke-width="1.2" fill="none">
    <line x1="542" y1="562" x2="648" y2="562"/>
    <polyline points="550,557 542,562 550,567"/>
    <polyline points="640,557 648,562 640,567"/>
    <line x1="1028" y1="607" x2="1028" y2="1095"/>
    <polyline points="1023,615 1028,607 1033,615"/>
    <polyline points="1023,1087 1028,1095 1033,1087"/>
    <line x1="224" y1="1166" x2="978" y2="1166"/>
    <polyline points="232,1161 224,1166 232,1171"/>
    <polyline points="970,1161 978,1166 970,1171"/>
  </g>
</svg>
<div class="dim-label" style="left:550px; top:530px; background:transparent;">1inches</div>
<div class="dim-label" style="left:994px; top:864px;">Hight 4.2inches</div>
<div class="dim-label" style="left:312px; top:1151px;">Wide 6.8inches</div>

</body>
</html>
```